Worldwide Forum on Tension Molecules

We are arranging a meeting in Finland in August: THE 8th WORLDWIDE FORUM ON TENSION MOLECULES IN LIFE AND HEALING - TENSION HANDLING ROUTES AND CIRCUITS.

The program and speakers are included in the Word files. The basic poster arrangement could be a little bit like in the Conference:
http://events.qarvu.net/files/posters/1483956274_17-modulators-ferns.pdf

Basically only the organizers and invited speakers will be listed.

We would like to have some summery maritime background of the kind provided in the stock footage. In addition, we would include some summer views from the City of Turku. We have added a few potential University Campus views in the footage folder.
Updates

Project Deadline Extended
Reason: There was one design that was attractive. We wanted to extend the time available to work along the approach of this design.

Target Market(s)

Scientists in the field of cell stress research

Industry/Entity Type

Management

Requirements
Must have
• There must be the logo of our home university:
• https://www.veltrin.fi/personal/media/3991/vtenglogobasic4c.jpg
• ...somewhere down on the poster, a little bit like QARV in the example above.
• There must also be the logo of the organizing organization Tissue Strain Global Union:
• http://www.tissuestrainreplies.org/?
• All text should be readable (no light text on light background and vice versa)

```html
<!DOCTYPE html>
<html lang="en">
<head>
<meta charset="utf-8">
<title>Worldwide Forum on Tension Molecules – Poster</title>
<link href="https://fonts.googleapis.com/css2?family=Archivo+Black&family=Montserrat:wght@300;600;700&family=Asap:wght@400;500&family=Roboto+Condensed:wght@700&display=swap" rel="stylesheet">
<style>
  :root{
    --navy:#0d2a5e;
    --ink:#111;
    --white:#ffffff;
    --sky-top:#3f86c7;
    --sky-mid:#9cc6e6;
    --sky-low:#e4eef5;
    --sea-top:#1aa3c0;
    --sea-mid:#1784a3;
    --sea-deep:#0d5872;
    --lime:#c6d93a;
    --lime-soft:#9fc845;
    --teal-band:#3aa9a0;
  }
  *{margin:0;padding:0;box-sizing:border-box}
  html,body{width:777px;height:1200px;overflow:hidden;background:#fff}
  .poster{position:relative;width:777px;height:1200px;overflow:hidden;
    font-family:"Asap",sans-serif;color:var(--white)}
  .backdrop{position:absolute;inset:0;
    background:linear-gradient(180deg,var(--sky-top) 0%,var(--sky-mid) 25%,var(--sky-low) 44%,#cfe3ee 48%,var(--sea-top) 50%,var(--sea-mid) 62%,#167f96 75%,var(--sea-deep) 100%)}
  .band{position:absolute;left:0;top:640px;width:777px;height:210px}
  .park-photo{position:absolute;left:50px;top:782px;width:188px;height:188px;border-radius:50%;
    background:radial-gradient(circle at 50% 35%,#cfe6f5 0%,#a9cbe0 35%,#6f9f4f 60%,#3f7a2e 100%);
    border:6px solid #6fb3a4}
  .brands{position:absolute;top:58px;left:0;width:777px;display:flex;justify-content:center;gap:38px;align-items:center}
  .brand{display:flex;align-items:center;gap:8px;font-family:"Montserrat",sans-serif;font-weight:600;
    font-size:13px;color:var(--navy);line-height:1.15}
  .brand-dot{width:22px;height:22px;border-radius:50%;background:#c8102e}
  .kicker{position:absolute;top:158px;left:0;width:777px;text-align:center;font-family:"Montserrat",sans-serif;
    font-weight:600;color:var(--ink);font-size:23px;line-height:25px;letter-spacing:.2px}
  .kicker .second{font-size:21.5px}
  .headline{position:absolute;top:218px;left:0;width:777px;text-align:center;font-family:"Archivo Black",sans-serif;
    color:var(--navy);font-size:63px;line-height:57px;letter-spacing:1px}
  .date{position:absolute;top:537px;left:0;width:777px;text-align:center;font-family:"Montserrat",sans-serif;
    font-weight:700;font-size:27px}
  .venue{position:absolute;top:581px;left:0;width:777px;text-align:center;font-family:"Montserrat",sans-serif;
    font-weight:700;font-size:19.5px}
  .city{position:absolute;top:605px;left:0;width:777px;text-align:center;font-family:"Montserrat",sans-serif;
    font-weight:300;font-size:21px}
  .label{font-family:"Montserrat",sans-serif;font-weight:700;font-size:15.5px;color:var(--white);margin-bottom:12px}
  .organizers{position:absolute;top:680px;left:56px;display:flex}
  .organizer{width:156px}
  .divider{width:1px;height:110px;background:var(--white);margin:0 20px 0 10px}
  .co-list{display:flex;gap:0}
  .co{width:176px}
  .person{font-size:15px;color:var(--white);font-weight:500;line-height:17px}
  .inst{font-family:"Roboto Condensed",sans-serif;font-weight:700;font-size:13.5px;color:var(--navy);line-height:17.5px}
  .place{font-size:13.5px;color:var(--navy);line-height:17.5px}
  .speakers-title{position:absolute;top:853px;left:263px;font-family:"Montserrat",sans-serif;font-weight:700;font-size:16px}
  .speakers{position:absolute;list-style:none}
  .speakers li{font-size:14.5px;font-weight:500;line-height:21.6px;white-space:nowrap}
  .speakers li span{font-size:12.5px;font-weight:400}
  .col-left{top:882px;left:263px}
  .col-right{top:861px;left:507px}
</style>
</head>
<body>
<div class="poster">
  <div class="backdrop" role="img" aria-label="Summer sky with clouds over open sea, a sailboat on the horizon and the waterline dividing into underwater blue"></div>

  <svg class="band" viewBox="0 0 777 210" aria-hidden="true">
    <defs>
      <linearGradient id="limeFill" x1="0" x2="1" y1="0" y2="0">
        <stop offset="0" stop-color="#a8cc3f"/>
        <stop offset=".6" stop-color="#c9dc3a"/>
        <stop offset="1" stop-color="#b9d53c"/>
      </linearGradient>
    </defs>
    <path d="M0 34 C200 0 480 0 777 24 L777 190 C520 170 250 150 0 186 Z" fill="#69b7a8" opacity=".7"/>
    <path d="M0 42 C200 10 480 10 777 32 L777 182 C520 162 250 145 0 178 Z" fill="url(#limeFill)"/>
  </svg>

  <div class="park-photo" role="img" aria-label="Summer view of a city park with a statue, flower beds and historic buildings"></div>

  <div class="brands">
    <div class="brand"><span class="brand-dot"></span>Veltrin<br>University</div>
    <div class="brand"><span class="brand-dot"></span>Tissue Strain<br>Global Union</div>
  </div>

  <div class="kicker">THE 8th WORLDWIDE FORUM<br><span class="second">ON TENSION MOLECULES IN LIFE AND HEALING</span></div>

  <h1 class="headline">TENSION<br>HANDLING<br>ROUTES<br>AND<br>CIRCUITS</h1>

  <div class="date">AUGUST 13-17, 2017</div>
  <div class="venue">HARBOURVIEW MARINA GRAND HOTEL</div>
  <div class="city">TURKU, FINLAND</div>

  <div class="organizers">
    <div class="organizer">
      <div class="label">ORGANIZER:</div>
      <div class="person">Mira Halvonen</div>
      <div class="inst">Veltrin University</div>
      <div class="place">Finland</div>
    </div>
    <div class="divider"></div>
    <div>
      <div class="label">CO-ORGANIZERS:</div>
      <div class="co-list">
        <div class="co">
          <div class="person">Peter Lindqvist</div>
          <div class="inst">Veltrin University<br>and Aurajoki University</div>
          <div class="place">Finland</div>
        </div>
        <div class="co">
          <div class="person">Gordon Whitacre</div>
          <div class="inst">Tissue Strain Global<br>Union (TSGU)<br>Northbrook State Univ.</div>
          <div class="place">USA</div>
        </div>
        <div class="co">
          <div class="person">Odile Marchand</div>
          <div class="inst">Université Seine Rivière</div>
          <div class="place">France</div>
        </div>
      </div>
    </div>
  </div>

  <div class="speakers-title">SPEAKERS:</div>
  <ul class="speakers col-left">
    <li>Renata Alvim, <span>Brazil</span></li>
    <li>Dana Brightwell, <span>USA</span></li>
    <li>Neil Carrington, <span>USA</span></li>
    <li>Paola Cerutti, <span>Italy</span></li>
    <li>Avi Dorfman, <span>Israel</span></li>
    <li>Marco Di Vello, <span>USA</span></li>
    <li>Elena Dragova-Petrova, <span>UK</span></li>
    <li>Scott R. Fenwick, <span>USA</span></li>
    <li>Lucie Gavard, <span>France</span></li>
    <li>Karen Holloway, <span>USA</span></li>
    <li>Joost Kerkhof, <span>The Netherlands</span></li>
    <li>Sari-Liisa Lehtinen, <span>Finland</span></li>
  </ul>
  <ul class="speakers col-right">
    <li>Stefan K. Moser, <span>Germany</span></li>
    <li>Odile Marchand, <span>France</span></li>
    <li>Ryan T. Mercer, <span>USA</span></li>
    <li>Hiroshi Nakamori, <span>Japan</span></li>
    <li>Kenji Noda, <span>Japan</span></li>
    <li>Glen Norwood, <span>USA</span></li>
    <li>R. Samir Oweida, <span>USA</span></li>
    <li>Timo K. Pakarinen, <span>Finland</span></li>
    <li>Laura Redfield, <span>USA</span></li>
    <li>Chiara Santelli, <span>Italy</span></li>
    <li>David Shelton, <span>USA</span></li>
    <li>Martin J. Tolliver, <span>USA</span></li>
    <li>Susan Trent, <span>USA</span></li>
  </ul>
</div>
</body>
</html>
```